Harvest Gathering event flyer

I would like a church event flyer designed. The event is called "HARVEST GATHERING 2018". I am looking for a professional, yet catchy design that uses our brand colors and logo creatively while communicating key information of the event effectively.

1. The logo is attached in two color formats. The designer has the choice to use them as he/she want.

2. The location of the event is: Lindqvist Community Center, 482 Tamsworth Street, Portland, ME 04102
3. Time and date of event. The designer can organize and format the date and time as he/she pleases.
December 28th, 29th @ 7:00PM
December 30th @ 10:00AM
4. The topic of the event is "Tongues of fire". The designer is free to use this phrase as he/she pleases to create a good composition.
5. Speaker: Prophet Marcus Obuya
6. Contact information: contact@cedarbrookfellowship.org - Telephone number: 207 555 0148

7. I would also like the following three words on the flyer. These words describe the focus of the event: FIRE, REVIVAL, PROPHETIC

```html
<!DOCTYPE html>
<html lang="en">
<head>
<meta charset="utf-8">
<title>Harvest Gathering 2018 – Tongues of Fire</title>
<link rel="stylesheet" href="https://fonts.googleapis.com/css2?family=Montserrat:wght@300;400;700;800;900&family=Oswald:wght@600;700&family=Cinzel:wght@500&display=swap">
<style>
  :root {
    --navy-deep: #082a4a;
    --navy: #0d3b63;
    --navy-light: #15507f;
    --white: #ffffff;
    --orange: #f7931e;
    --orange-deep: #e8571d;
    --red: #e2261f;
    --ember: #3b0b0b;
    --black: #050608;
    --glow: #6f8cff;
    --silver: #d7d9dc;
    --ink: #0b2f52;
  }
  * { box-sizing: border-box; margin: 0; padding: 0; }
  html, body { width: 877px; height: 1200px; overflow: hidden; background: var(--navy-deep); }
  .flyer {
    position: relative; width: 877px; height: 1200px; overflow: hidden;
    background: radial-gradient(ellipse at 70% 30%, var(--navy-light) 0%, var(--navy) 45%, var(--navy-deep) 100%);
    font-family: "Montserrat", sans-serif; color: var(--white);
  }
  .backdrop, .art { position: absolute; inset: 0; width: 877px; height: 1200px; }

  .brand {
    position: absolute; left: 69px; top: 0; width: 318px; height: 277px;
    display: flex; align-items: center; justify-content: center; gap: 12px;
    padding-bottom: 40px;
  }
  .brand-dot { width: 18px; height: 18px; border-radius: 50%; background: var(--orange); }
  .brand-name {
    font-family: "Montserrat", sans-serif; font-weight: 400; font-size: 46px;
    letter-spacing: 2px; color: var(--white);
  }

  .speaker-photo {
    position: absolute; left: 400px; top: 140px; width: 477px; height: 450px;
    background: radial-gradient(ellipse at 50% 40%, #6b4a38 0%, #3a2a24 30%, #1d2430 60%, rgba(13,59,99,0) 78%);
  }

  .headline { position: absolute; left: 66px; top: 316px; width: 330px; height: 230px; }
  .headline text { font-family: "Montserrat", sans-serif; font-weight: 800; fill: var(--white); }

  .flames {
    position: absolute; left: 54px; top: 572px; width: 282px; height: 100px;
    background: linear-gradient(to top, #f9e21b 0%, #f7931e 45%, #e8341d 80%, rgba(226,38,31,0) 100%);
    border-radius: 50% 50% 8px 8px / 70% 70% 8px 8px;
  }
  .topic {
    position: absolute; left: 43px; top: 655px; width: 316px; height: 142px;
    border-radius: 14px; padding: 7px;
    background: linear-gradient(to bottom, #f7b21e, var(--orange-deep) 60%, var(--red));
  }
  .topic-inner {
    width: 100%; height: 100%; border-radius: 9px;
    background: linear-gradient(to bottom, var(--ember), #120404);
    display: flex; flex-direction: column; align-items: center; justify-content: center;
    line-height: 1;
  }
  .topic-top { font-weight: 900; font-size: 46px; color: var(--orange); letter-spacing: -1px; }
  .topic-bottom { font-weight: 400; font-size: 58px; color: var(--white); margin-top: 2px; }

  .speaker-text { font-family: "Oswald", sans-serif; font-weight: 700; }
  .speaker-title { fill: var(--silver); }
  .speaker-name { fill: url(#nameGold); }

  .focus {
    position: absolute; left: 0; width: 877px; top: 850px; text-align: center;
    font-family: "Cinzel", serif; font-weight: 500; font-size: 35px; letter-spacing: 1px;
  }

  .details { position: absolute; left: 0; top: 968px; width: 877px; display: flex; font-weight: 300; font-size: 20px; line-height: 25px; letter-spacing: .3px; }
  .venue { width: 427px; text-align: right; padding-right: 12px; font-style: normal; }
  .divider { width: 3px; height: 100px; background: var(--white); margin-top: 3px; }
  .schedule { padding-left: 14px; }

  .contact-bar {
    position: absolute; left: 0; top: 1115px; width: 877px; height: 58px; background: var(--white);
    display: flex; align-items: center; justify-content: center;
    font-weight: 800; font-size: 22px; color: var(--ink);
  }
  .footer-band { position: absolute; left: 0; top: 1173px; width: 877px; height: 19px; background: var(--ink); }
  .footer-line { position: absolute; left: 0; top: 1192px; width: 877px; height: 8px; background: var(--white); }
</style>
</head>
<body>
<main class="flyer">

  <svg class="backdrop" viewBox="0 0 877 1200" aria-hidden="true">
    <polygon points="380,0 520,0 877,330 877,430" fill="#ffffff" opacity="0.05"/>
    <polygon points="560,0 640,0 877,180 877,240" fill="#ffffff" opacity="0.04"/>
    <polygon points="0,980 877,900 877,960 0,1060" fill="#000000" opacity="0.08"/>
    <polygon points="140,832 700,827 690,912 150,922" fill="#0a2f55" opacity="0.8"/>
    <path d="M69 0 V277 L228 302 L387 277 V0" fill="#0f3d66" stroke="#ffffff" stroke-width="4"/>
  </svg>

  <div class="brand">
    <span class="brand-dot"></span>
    <span class="brand-name">KELVARA</span>
  </div>

  <div class="speaker-photo" role="img" aria-label="Portrait photograph of the speaker, smiling, in glasses, dark blazer and light blue shirt"></div>

  <svg class="headline" viewBox="0 0 330 230">
    <text x="2" y="58" font-size="64" textLength="318" lengthAdjust="spacingAndGlyphs">HARVEST</text>
    <text x="2" y="110" font-size="46" textLength="318" lengthAdjust="spacingAndGlyphs">GATHERING</text>
    <text x="0" y="218" font-size="112" textLength="322" lengthAdjust="spacingAndGlyphs">2018</text>
  </svg>

  <svg class="art" viewBox="0 0 877 1200">
    <defs>
      <linearGradient id="plate" x1="0" y1="0" x2="0" y2="1">
        <stop offset="0" stop-color="#2b2f33"/>
        <stop offset="0.45" stop-color="#0a0b0d"/>
        <stop offset="1" stop-color="#000000"/>
      </linearGradient>
      <linearGradient id="nameGold" x1="0" y1="0" x2="0" y2="1">
        <stop offset="0" stop-color="#ffbf3c"/>
        <stop offset="0.6" stop-color="#f7931e"/>
        <stop offset="1" stop-color="#e6771a"/>
      </linearGradient>
    </defs>
    <polygon points="338,600 877,548 877,760 392,800" fill="url(#plate)" aria-hidden="true"/>
    <polygon points="435,560 877,598 877,777 350,780" fill="none" stroke="var(--glow)" stroke-width="2.5" opacity="0.9" aria-hidden="true"/>
    <polygon points="435,560 877,598 877,777 350,780" fill="none" stroke="#ffffff" stroke-width="1" aria-hidden="true"/>
    <line x1="770" y1="782" x2="710" y2="930" stroke="#8fb7ff" stroke-width="2" opacity="0.6" aria-hidden="true"/>

    <g class="speaker-text">
      <text class="speaker-title" transform="translate(506 680) rotate(-6) skewX(-10)" font-size="62" textLength="214" lengthAdjust="spacingAndGlyphs">PROPHET</text>
      <text class="speaker-name" transform="translate(408 752) rotate(-5) skewX(-10)" font-size="84" textLength="438" lengthAdjust="spacingAndGlyphs">MARCUS OBUYA</text>
    </g>
  </svg>

  <div class="flames" role="img" aria-label="Illustrated row of orange and yellow flames"></div>
  <div class="topic">
    <div class="topic-inner">
      <span class="topic-top">TONGUES</span>
      <span class="topic-bottom">OF FIRE</span>
    </div>
  </div>

  <p class="focus">FIRE, REVIVAL, PROPHETIC</p>

  <section class="details">
    <address class="venue">
      Lindqvist Community Center,<br>482 Tamsworth Street,<br>Portland,<br>ME 04102
    </address>
    <span class="divider"></span>
    <p class="schedule">December 28th, 29th<br>@ 7:00PM<br>December 30th<br>@ 10:00AM</p>
  </section>

  <footer>
    <div class="contact-bar">contact@cedarbrookfellowship.org - Call: 207 555 0148</div>
    <div class="footer-band"></div>
    <div class="footer-line"></div>
  </footer>

</main>
</body>
</html>
```